Design mobile friendly review and ranking site

We're working on a corporate website for reviewing and ranking fellow employees. We need the website to look both fun and professional and it needs to be responsive - to it works on mobile and desktop.

Looking for css and HTML for 3 key pages as well as a header and footer for the site. Also would need any supporting graphics as part of the design.

Target Market(s)

Professionals in their 20s, 30s, and 40s.

Industry/Entity Type

Internet

Coding

Coded - Design and coding required

Number of Pages Required

3 page

Font styles to use
Sans Serif

Requirements
Must have
• 3 key pages we need (note included screenshots for each - these are just super rough cuts so you see examples of the content.)
• a) main-intro: A compelling into page with a login/registration form. Should be sleek/modern/enticing. Also we would show the ranking for the top 3 people to tease people re: content.
• b) main-page: Has two sections: One at the top where you would rate someone and one at the bottom where it shows a ranking of people.
• c) profile page: This is where you view a specific person. You see the person's picture, some info about the person, you see their overall rating, you can rate them, and you also see their historical ratings.
Nice to have
• Note we need css and HTML for this. It should feel as sleek and modern. Note also must be responsive design so it works well in mobile and desktop.

```html
<!DOCTYPE html>
<html lang="en">
<head>
<meta charset="utf-8">
<title>Team Tally</title>
<link href="https://fonts.googleapis.com/css2?family=Open+Sans:wght@400;600;700&display=swap" rel="stylesheet">
<style>
:root{
  --blue:#2a94ee;
  --blue-dark:#1b7fd9;
  --level:#1766c2;
  --page:#f2f2f2;
  --card:#ffffff;
  --ink:#2c3a4a;
  --muted:#7b7f85;
  --line:#e3e6e9;
  --star:#fbb817;
  --star-off:#c3c6cb;
  --gold:#f6d81f;
  --rank1:#1fc1d7;
  --rank2:#8bc34a;
  --rank3:#ff9a0c;
  --rank4:#5f7d8e;
}
*{box-sizing:border-box;margin:0;padding:0}
html,body{width:1200px;height:913px;overflow:hidden}
body{position:relative;background:var(--page);font-family:"Open Sans",sans-serif;color:var(--ink);font-size:12px}
.star-defs{position:absolute;width:0;height:0}

/* header */
.site-header{position:absolute;left:0;top:0;width:1200px;height:58px;background:var(--blue);color:#fff}
.brand{position:absolute;left:91px;top:17px;font-size:18px;font-weight:600;letter-spacing:.2px;color:#fff}
.share-btn{position:absolute;left:303px;top:11px;width:206px;height:34px;background:var(--blue-dark);border-radius:3px;display:flex;align-items:center;justify-content:center;gap:8px;font-size:12px}
.user-badge{position:absolute;left:845px;top:10px;width:37px;height:37px;border-radius:50%;background:#fff;border:3px solid #bfe0fb;display:flex;align-items:center;justify-content:center}
.progress{position:absolute;left:895px;top:19px;width:144px;height:2px;background:#6ab6f5}
.progress span{display:block;width:78px;height:2px;background:var(--level)}
.progress-text{position:absolute;left:895px;top:26px;font-size:12px;color:#e4f1fd}
.progress-text b{color:#fff;font-weight:700}
.level{position:absolute;left:1049px;top:9px;width:39px;height:39px;border-radius:50%;background:var(--level);border:2px solid #4aa3ef;font-size:16px;font-weight:600;display:flex;align-items:center;justify-content:center}
.menu-dots{position:absolute;left:1107px;top:20px}

/* card */
.card{position:absolute;left:89px;width:1022px;background:var(--card)}
.rate-card{top:76px;height:217px}
.rate-photo{position:absolute;left:19px;top:19px;width:173px;height:173px;border:4px solid #fde9a2;background:linear-gradient(135deg,#c9c3b5 0%,#7d7a72 45%,#3f4650 100%)}
.add-btn{position:absolute;left:8px;top:9px;width:30px;height:30px;border-radius:50%;background:var(--gold);color:#fff;font-size:16px;display:flex;align-items:center;justify-content:center}
.rate-panel{position:absolute;left:212px;top:16px;width:146px}
.rate-name{font-size:16px;font-weight:400;margin-bottom:7px}
.trait{border-bottom:1px solid var(--line);padding:1px 0 9px;margin-bottom:9px}
.trait-label{font-size:12px;color:#555b62;margin-bottom:3px}
.comment{position:absolute;left:405px;top:25px;width:591px}
.comment-label{font-size:12px;color:#555b62}
.comment-box{margin-top:13px;width:591px;height:92px;border:1px solid var(--line);padding:12px;color:#a9adb2;font-size:11px}
.actions{display:flex;gap:9px;margin-top:16px;margin-left:1px}
.btn{width:74px;height:35px;border:1px solid var(--line);border-radius:2px;display:flex;align-items:center;justify-content:center;font-size:12px;color:#555b62;background:#fff}
.btn-save{background:#e4e4e4;border-color:#e4e4e4}

/* rankings */
.rank-card{top:315px;height:511px}
.filters{height:62px;border-bottom:1px solid var(--line);position:relative}
.select{position:absolute;top:11px;height:39px;border:1px solid #dcdfe2;padding:0 16px;display:flex;align-items:center;justify-content:space-between;color:#6a6f75;font-size:12px}
.select::after{content:"";border:3.5px solid transparent;border-top:4px solid #555;margin-top:4px}
.filter-word{position:absolute;top:23px;font-size:12px;color:#6a6f75}
.board{position:absolute;left:22px;top:62px;width:978px;display:grid;grid-template-columns:478px 478px;column-gap:22px}
.member{position:relative;height:213px}
.member.top{border-bottom:1px solid var(--line)}
.member-photo{position:absolute;left:19px;top:25px;width:87px;height:87px;border:3px solid}
.rank-badge{position:absolute;left:117px;top:29px;width:25px;height:25px;border-radius:50%;color:#fff;font-size:13px;display:flex;align-items:center;justify-content:center}
.member-name{position:absolute;left:150px;top:31px;font-size:14px}
.stat{position:absolute;left:118px;font-size:12px;color:var(--muted)}
.score{position:absolute;left:118px;width:230px;display:flex;align-items:center;font-size:12px;color:#44494f}
.score .label{width:109px}
.stars{display:flex;gap:4px}
.stars svg{width:14px;height:14px}
.on{fill:var(--star)}
.off{fill:var(--star-off)}

/* footer */
.site-footer{position:absolute;left:0;top:873px;width:1200px;height:40px;background:var(--blue);color:#fff;font-size:12px;display:flex;align-items:center;justify-content:center}
</style>
</head>
<body>
<svg class="star-defs" aria-hidden="true"><defs><symbol id="star" viewBox="0 0 20 20"><path d="M10 1l2.7 6 6.3.6-4.8 4.3 1.4 6.4L10 15l-5.6 3.3 1.4-6.4L1 7.6 7.3 7z"/></symbol></defs></svg>

<header class="site-header">
  <div class="brand">Team Tally</div>
  <div class="share-btn">
    <svg width="14" height="14" viewBox="0 0 14 14" fill="none" stroke="#fff" stroke-width="1"><circle cx="3" cy="7" r="2"/><circle cx="11" cy="3" r="2"/><circle cx="11" cy="11" r="2"/><path d="M4.8 6l4.4-2.2M4.8 8l4.4 2.2"/></svg>
    Share this to get more points
  </div>
  <div class="user-badge"><svg width="12" height="13" viewBox="0 0 12 13" fill="var(--blue)"><circle cx="6" cy="3.5" r="3"/><path d="M0 13c0-4 2.5-5.5 6-5.5s6 1.5 6 5.5z"/></svg></div>
  <div class="progress"><span></span></div>
  <div class="progress-text"><b>41</b> points to level <b>4</b></div>
  <div class="level">3</div>
  <svg class="menu-dots" width="4" height="17" viewBox="0 0 4 17" fill="#fff"><circle cx="2" cy="2" r="1.8"/><circle cx="2" cy="8.5" r="1.8"/><circle cx="2" cy="15" r="1.8"/></svg>
</header>

<section class="card rate-card">
  <div class="rate-photo" role="img" aria-label="Photo of Michael sitting on a sofa with a laptop"></div>
  <div class="add-btn">+</div>
  <div class="rate-panel">
    <h2 class="rate-name">Michael</h2>
    <div class="trait"><div class="trait-label">Smart</div>
      <div class="stars"><svg class="on"><use href="#star"/></svg><svg class="on"><use href="#star"/></svg><svg class="on"><use href="#star"/></svg><svg class="off"><use href="#star"/></svg><svg class="off"><use href="#star"/></svg></div></div>
    <div class="trait"><div class="trait-label">Average Personality</div>
      <div class="stars"><svg class="on"><use href="#star"/></svg><svg class="on"><use href="#star"/></svg><svg class="on"><use href="#star"/></svg><svg class="off"><use href="#star"/></svg><svg class="off"><use href="#star"/></svg></div></div>
    <div class="trait"><div class="trait-label">Works Crazy Hard</div>
      <div class="stars"><svg class="on"><use href="#star"/></svg><svg class="on"><use href="#star"/></svg><svg class="on"><use href="#star"/></svg><svg class="off"><use href="#star"/></svg><svg class="off"><use href="#star"/></svg></div></div>
  </div>
  <div class="comment">
    <div class="comment-label">(Optional) Write an anonymous comment about this person</div>
    <div class="comment-box">Write Review...</div>
    <div class="actions"><div class="btn">Skip</div><div class="btn btn-save">Save</div></div>
  </div>
</section>

<section class="card rank-card">
  <div class="filters">
    <div class="select" style="left:87px;width:226px">Best</div>
    <div class="filter-word" style="left:336px">In</div>
    <div class="select" style="left:358px;width:262px">All functions</div>
    <div class="filter-word" style="left:649px">and</div>
    <div class="select" style="left:677px;width:262px">All levels</div>
  </div>
  <div class="board">
    <article class="member top">
      <div class="member-photo" style="border-color:#a8e6ef;background:linear-gradient(135deg,#2c2a24,#5b5346 55%,#1c1b18)" role="img" aria-label="Photo of Jim Johns in a suit"></div>
      <div class="rank-badge" style="background:var(--rank1)">1</div>
      <div class="member-name">Jim Johns</div>
      <div class="stat" style="top:60px">Points: 41</div>
      <div class="stat" style="top:88px">Number of reviews: 5</div>
      <div class="score" style="top:118px"><span class="label">Smarts:</span><div class="stars"><svg class="on"><use href="#star"/></svg><svg class="on"><use href="#star"/></svg><svg class="on"><use href="#star"/></svg><svg class="off"><use href="#star"/></svg><svg class="off"><use href="#star"/></svg></div></div>
      <div class="score" style="top:145px"><span class="label">Easy to work with:</span><div class="stars"><svg class="on"><use href="#star"/></svg><svg class="on"><use href="#star"/></svg><svg class="on"><use href="#star"/></svg><svg class="off"><use href="#star"/></svg><svg class="off"><use href="#star"/></svg></div></div>
      <div class="score" style="top:172px"><span class="label">Hard worker:</span><div class="stars"><svg class="on"><use href="#star"/></svg><svg class="on"><use href="#star"/></svg><svg class="on"><use href="#star"/></svg><svg class="off"><use href="#star"/></svg><svg class="off"><use href="#star"/></svg></div></div>
    </article>
    <article class="member top">
      <div class="member-photo" style="border-color:#d6ebc0;background:linear-gradient(160deg,#7c8a73,#3f4a3a 55%,#56594f)" role="img" aria-label="Photo of Mcihael standing in a forest road"></div>
      <div class="rank-badge" style="background:var(--rank2)">2</div>
      <div class="member-name">Mcihael</div>
      <div class="stat" style="top:60px">Points: 4</div>
      <div class="stat" style="top:88px">Number of reviews: 5</div>
      <div class="score" style="top:118px"><span class="label">Smarts:</span><div class="stars"><svg class="on"><use href="#star"/></svg><svg class="on"><use href="#star"/></svg><svg class="on"><use href="#star"/></svg><svg class="off"><use href="#star"/></svg><svg class="off"><use href="#star"/></svg></div></div>
      <div class="score" style="top:145px"><span class="label">Easy to work with:</span><div class="stars"><svg class="on"><use href="#star"/></svg><svg class="on"><use href="#star"/></svg><svg class="on"><use href="#star"/></svg><svg class="off"><use href="#star"/></svg><svg class="off"><use href="#star"/></svg></div></div>
      <div class="score" style="top:172px"><span class="label">Hard worker:</span><div class="stars"><svg class="on"><use href="#star"/></svg><svg class="on"><use href="#star"/></svg><svg class="on"><use href="#star"/></svg><svg class="off"><use href="#star"/></svg><svg class="off"><use href="#star"/></svg></div></div>
    </article>
    <article class="member">
      <div class="member-photo" style="border-color:#fcd9a8;background:linear-gradient(135deg,#344845,#1f2b2c 55%,#4a3a2a)" role="img" aria-label="Photo of Joe Nolan sitting outdoors"></div>
      <div class="rank-badge" style="background:var(--rank3)">3</div>
      <div class="member-name">Joe Nolan</div>
      <div class="stat" style="top:60px">Points: 3.6</div>
      <div class="stat" style="top:88px">Number of reviews: 5</div>
      <div class="score" style="top:118px"><span class="label">Smarts:</span><div class="stars"><svg class="on"><use href="#star"/></svg><svg class="on"><use href="#star"/></svg><svg class="off"><use href="#star"/></svg><svg class="off"><use href="#star"/></svg><svg class="off"><use href="#star"/></svg></div></div>
      <div class="score" style="top:145px"><span class="label">Easy to work with:</span><div class="stars"><svg class="on"><use href="#star"/></svg><svg class="on"><use href="#star"/></svg><svg class="on"><use href="#star"/></svg><svg class="off"><use href="#star"/></svg><svg class="off"><use href="#star"/></svg></div></div>
      <div class="score" style="top:172px"><span class="label">Hard worker:</span><div class="stars"><svg class="on"><use href="#star"/></svg><svg class="on"><use href="#star"/></svg><svg class="on"><use href="#star"/></svg><svg class="off"><use href="#star"/></svg><svg class="off"><use href="#star"/></svg></div></div>
    </article>
    <article class="member">
      <div class="member-photo" style="border-color:#c9d3d9;background:linear-gradient(180deg,#c9ccc8,#8c9784 55%,#4f5a45)" role="img" aria-label="Photo of Kevin Doe reading in a park"></div>
      <div class="rank-badge" style="background:var(--rank4)">4</div>
      <div class="member-name">Kevin Doe</div>
      <div class="stat" style="top:60px">Points: 2</div>
      <div class="stat" style="top:88px">Number of reviews: 5</div>
      <div class="score" style="top:118px"><span class="label">Smarts:</span><div class="stars"><svg class="on"><use href="#star"/></svg><svg class="on"><use href="#star"/></svg><svg class="off"><use href="#star"/></svg><svg class="off"><use href="#star"/></svg><svg class="off"><use href="#star"/></svg></div></div>
      <div class="score" style="top:145px"><span class="label">Easy to work with:</span><div class="stars"><svg class="on"><use href="#star"/></svg><svg class="on"><use href="#star"/></svg><svg class="on"><use href="#star"/></svg><svg class="off"><use href="#star"/></svg><svg class="off"><use href="#star"/></svg></div></div>
      <div class="score" style="top:172px"><span class="label">Hard worker:</span><div class="stars"><svg class="on"><use href="#star"/></svg><svg class="on"><use href="#star"/></svg><svg class="off"><use href="#star"/></svg><svg class="off"><use href="#star"/></svg><svg class="off"><use href="#star"/></svg></div></div>
    </article>
  </div>
</section>

<footer class="site-footer">© Team Tally, All Rights Reserved.</footer>
</body>
</html>
```